We need a brand logo for a range of health supplements we are launching.

The brand is called 'Mind Crate' The tagline for our brand is "The Entrepreneurs Supplement"

The brand is aimed at Entrepreneurs who would use our supplements to ultimately increase their brain power and turn them into more successful entrepreneurs.

As an additional note. The first product we launch is going to be a brain supplement that supports mental focus, promotes clarity and aids memory function. It's going to be called the Mind Crate Am Formula. This is a supplement which will be taken by entrepreneurs in the morning. The logo must therefore be suitable to incorporate it into the packaging design for our first product.

The product itself is a bottle of 60 capsules that comes in a box. (Therefore, it's a plastic bottle inside a cardboard box).

The bottle is black and comes with a black cap. I have attached an example of the bottle.

Also attached is the label template for the bottle. Everything that is displayed on the right and left hand side of the bottle must be visible. Everything in the middle can be deleted and re-designed except for 'Dietary supplement 60 Capsules' which must also be displayed.

Also attached is the box template. The box template is where all the creative design work should take place which can then be replicated onto the bottle.

The finished project should be a 3D render of the box and bottle side by side.

We would require the box and label templates to give to out manufacturer for printing.

Target Market(s)

Entrepreneurs

Industry/Entity Type

Health And Wellness

Logo Text

Mind Crate - The Entrepreneurs Supplement

Colors
3176b5
0255a3
85abd2
ffffff
e8e8e8
959595
f6f6f6
919191

Requirements
Must have
• This product must be aimed at entrepreneurs.
• The colur scheme should be Blue, Grey and White. The color schemes I have suggested

```html
<!DOCTYPE html>
<html lang="en">
<head>
<meta charset="utf-8">
<title>Mind Crate – The Entrepreneurs Supplement</title>
<link rel="stylesheet" href="https://fonts.googleapis.com/css2?family=Marcellus+SC&family=Oswald:wght@500&display=swap">
<style>
  :root {
    --bg: #f6f6f6;
    --panel: #0b0b0b;
    --panel-edge: #1c1c1c;
    --white: #ffffff;
    --silver-light: #e8e8e8;
    --silver-mid: #959595;
    --silver-dark: #919191;
    --ink: #111111;
    --blue: #3176b5;
    --blue-deep: #0255a3;
    --blue-soft: #85abd2;
  }
  * { margin: 0; padding: 0; box-sizing: border-box; }
  html, body { width: 1200px; height: 960px; overflow: hidden; background: var(--bg); }
  .canvas { position: relative; width: 1200px; height: 960px; background: linear-gradient(180deg, var(--bg) 0%, var(--silver-light) 100%); }

  .box-front {
    position: absolute; left: 280px; top: 60px; width: 640px; height: 840px;
    background: linear-gradient(180deg, var(--panel-edge) 0%, var(--panel) 100%);
    overflow: hidden;
  }
  .brand-name {
    position: absolute; left: 0; right: 0; top: 92px; text-align: center;
    font-family: "Marcellus SC", serif; font-size: 78px; font-weight: 400;
    color: var(--white); letter-spacing: 3px; line-height: 1;
  }
  .tagline-band {
    position: absolute; left: 40px; right: 40px; top: 218px; height: 42px;
    background: linear-gradient(90deg, var(--silver-mid) 0%, var(--white) 35%, var(--silver-light) 60%, var(--silver-dark) 100%);
    display: flex; align-items: center; justify-content: center;
  }
  .tagline {
    font-family: "Marcellus SC", serif; font-size: 26px; color: var(--ink); letter-spacing: 2px; white-space: nowrap;
  }
  .content-badge {
    position: absolute; left: 26px; top: 315px; width: 170px; height: 170px; border-radius: 50%;
    background: radial-gradient(circle at 35% 30%, var(--white) 0%, var(--silver-light) 40%, var(--silver-mid) 100%);
    border: 3px solid var(--silver-dark);
    display: flex; flex-direction: column; align-items: center; justify-content: center;
    font-family: "Oswald", sans-serif; font-weight: 500; font-size: 26px; line-height: 1.05;
    color: var(--ink); text-transform: uppercase; text-align: center;
  }
  .head-illustration {
    position: absolute; left: 220px; top: 300px; width: 310px; height: 355px;
    border-radius: 155px 155px 0 0;
    background: radial-gradient(ellipse at 60% 30%, var(--blue-soft) 0%, var(--blue) 30%, var(--blue-deep) 50%, var(--panel-edge) 80%);
    opacity: 0.85;
  }
  .benefits-band {
    position: absolute; left: 0; right: 0; top: 655px; height: 140px;
    background: linear-gradient(90deg, var(--silver-mid) 0%, var(--white) 35%, var(--silver-light) 65%, var(--silver-dark) 100%);
    display: flex; flex-direction: column; align-items: center; justify-content: center;
  }
  .benefit {
    font-family: "Marcellus SC", serif; font-size: 32px; color: var(--ink); letter-spacing: 2px; line-height: 1.15;
  }
  .base-strip { position: absolute; left: 0; right: 0; bottom: 0; height: 45px; background: var(--panel); }
</style>
</head>
<body>
<main class="canvas">
  <section class="box-front">
    <h1 class="brand-name">Mind Crate</h1>
    <div class="tagline-band"><p class="tagline">The Entrepreneurs Supplement</p></div>
    <div class="content-badge"><span>Dietary</span><span>Supplement</span><span>60 Capsules</span></div>
    <div class="head-illustration" role="img" aria-label="Outline of a head in profile with a glowing blue brain"></div>
    <div class="benefits-band">
      <p class="benefit">Supports Mental Focus*</p>
      <p class="benefit">Promotes Clarity*</p>
      <p class="benefit">Memory Function Aid*</p>
    </div>
    <div class="base-strip"></div>
  </section>
</main>
</body>
</html>
```